Varnel Supply requires a new business card.

We are an online professional tool store.

Target Market(s)

We target the professional technician.

Industry/Entity Type

Business

Contact Information for Business Card

VarnelSupply.com.au

sales@varnelsupply.example

Requirements
Must have
• Needs to look commercial and professional
Should not have
• No Australian Colors, maps or shapes.
• No Shapes of Tools

```html
<!DOCTYPE html>
<html lang="en">
<head>
<meta charset="utf-8">
<title>Varnel Supply – Business Card</title>
<link rel="stylesheet" href="https://fonts.googleapis.com/css2?family=Arimo:wght@400;700&display=swap">
<style>
  :root {
    --page-bg: #2a2522;
    --card-bg: #222224;
    --brand-blue: #2f4fc4;
    --accent-cyan: #1aa3dc;
    --text-light: #f2f2f2;
    --divider: #8a8a8a;
  }
  * { box-sizing: border-box; margin: 0; padding: 0; }
  html, body { width: 1200px; height: 764px; overflow: hidden; }
  body {
    background: var(--page-bg);
    font-family: "Arimo", Arial, sans-serif;
    position: relative;
  }
  .card {
    position: absolute;
    top: 234px;
    width: 520px;
    height: 297px;
    background: var(--card-bg);
    border-radius: 3px;
    box-shadow: 0 6px 18px rgba(0,0,0,.45);
  }
  .card--back { left: 50px; }
  .card--front { left: 630px; display: flex; align-items: center; justify-content: center; }

  .brand {
    display: flex;
    align-items: center;
    gap: 10px;
    color: var(--brand-blue);
    font-weight: 700;
    white-space: nowrap;
  }
  .brand__dot {
    width: 16px; height: 16px;
    border-radius: 50%;
    background: var(--brand-blue);
    flex: none;
  }
  .card--back .brand {
    position: absolute;
    left: 34px; top: 128px;
    font-size: 30px;
  }
  .card--front .brand { font-size: 30px; }

  .divider {
    position: absolute;
    left: 268px; top: 40px;
    width: 1px; height: 217px;
    background: var(--divider);
  }
  .contact {
    position: absolute;
    left: 296px; top: 76px;
    color: var(--text-light);
  }
  .contact__name { font-size: 17px; font-weight: 700; }
  .contact__role { font-size: 13px; color: var(--accent-cyan); margin-top: 2px; }
  .contact__list { list-style: none; margin-top: 26px; }
  .contact__item {
    display: flex; align-items: center; gap: 9px;
    font-size: 13px; line-height: 20px;
  }
  .contact__icon { width: 14px; height: 14px; flex: none; }
  .contact__item--plain { padding-left: 23px; }
</style>
</head>
<body>
  <section class="card card--back">
    <div class="brand"><span class="brand__dot"></span>Varnel Supply</div>
    <div class="divider"></div>
    <div class="contact">
      <p class="contact__name">Joren Malvik</p>
      <p class="contact__role">Service Manager</p>
      <ul class="contact__list">
        <li class="contact__item">
          <svg class="contact__icon" viewBox="0 0 14 14" aria-hidden="true"><rect width="14" height="14" rx="2" fill="var(--accent-cyan)"/><path d="M3 4.5h8v5H3z M3 4.5l4 3 4-3" fill="none" stroke="var(--card-bg)" stroke-width="1.2"/></svg>
          sales@varnelsupply.example
        </li>
        <li class="contact__item">
          <svg class="contact__icon" viewBox="0 0 14 14" aria-hidden="true"><rect width="14" height="14" rx="2" fill="var(--accent-cyan)"/><circle cx="7" cy="7" r="3.8" fill="none" stroke="var(--card-bg)" stroke-width="1.2"/><path d="M3.2 7h7.6M7 3.2v7.6" stroke="var(--card-bg)" stroke-width="1"/></svg>
          VarnelSupply.com.au
        </li>
        <li class="contact__item">
          <svg class="contact__icon" viewBox="0 0 14 14" aria-hidden="true"><rect width="14" height="14" rx="2" fill="var(--accent-cyan)"/><rect x="4.5" y="2.8" width="5" height="8.4" rx="1" fill="none" stroke="var(--card-bg)" stroke-width="1.2"/></svg>
          0400 555 127
        </li>
        <li class="contact__item contact__item--plain">ABN 00000000000</li>
      </ul>
    </div>
  </section>

  <section class="card card--front">
    <div class="brand"><span class="brand__dot"></span>Varnel Supply</div>
  </section>
</body>
</html>
```